Beautiful Quotes For Social Media Posts

We are looking for 5 beautifully designed quotes for our social media account.

Inspiration of styles we like in both style and color along with a few of our favorite fonts (you are NOT limited to these fonts this is just to give you an idea):
https://quillmorestudio.example.com/s/k7p2vx9tqa41mzn8wbd3ce6hr5lf0y2j

*These fonts are property of Quillmore Studio. You do not have permission/rights to use them outside of this assignment*

Quotes to use (5):
“Only those who dare to fail greatly can ever achieve greatly.” –Vernon T. Ashgrove
“Don’t go through life, grow through life.” – Milo Pendrake
“Follow your bliss and the universe will open doors where there were only walls.” – Arthur Venholm
“If you don’t like the road you’re walking, start paving another one.” – Greta Mossley
“Life is like riding a bicycle. To keep your balance, you must keep moving.” —Lucian Thornwick

File Specifics:
- JPG
- 10x10 in size (square)
- Please include @QuillmoreStudio in the bottom right left or center of each design

Brand Details:
Soft but rich pastel and bright colors.
Hand Drawn florals, doodles and art
Handwritten looking fonts
Artsy, Creative, Girl and Inspiring

```html
<!DOCTYPE html>
<html lang="en">
<head>
<meta charset="utf-8">
<title>Grow Through Life — Quote Post</title>
<link rel="stylesheet" href="https://fonts.googleapis.com/css2?family=Lilita+One&family=Open+Sans:wght@700&display=swap">
<style>
  :root {
    --bg: #e1e1e1;
    --sage-deep: #7c9e97;
    --sage-light: #b4cac3;
    --coral: #f7845c;
    --forest: #0e4645;
    --clay: #c08b6b;
    --blush: #fba29b;
    --mustard: #c59b49;
    --brick: #cf6661;
  }
  * { margin: 0; padding: 0; box-sizing: border-box; }
  html, body { width: 1200px; height: 1200px; overflow: hidden; background: var(--bg); }
  .post {
    position: relative;
    width: 1200px;
    height: 1200px;
    background: var(--bg);
    overflow: hidden;
  }
  .wave { position: absolute; inset: 0; width: 1200px; height: 1200px; }
  .wave__band { fill: var(--sage-deep); }
  .wave__fill { fill: var(--sage-light); }
  .quote {
    position: absolute;
    left: 124px;
    top: 226px;
    font-family: "Lilita One", "Arial Black", sans-serif;
    font-size: 120px;
    line-height: 141px;
    text-transform: uppercase;
    letter-spacing: 1px;
  }
  .quote__line { display: block; white-space: nowrap; }
  .c-coral { color: var(--coral); }
  .c-forest { color: var(--forest); }
  .c-clay { color: var(--clay); }
  .c-blush { color: var(--blush); }
  .c-sage { color: var(--sage-deep); }
  .c-mustard { color: var(--mustard); }
  .c-brick { color: var(--brick); }
  .author {
    position: absolute;
    left: 126px;
    top: 948px;
    font-family: "Open Sans", Arial, sans-serif;
    font-weight: 700;
    font-size: 31px;
    letter-spacing: -0.5px;
    color: var(--sage-deep);
    text-transform: uppercase;
  }
  .handle {
    position: absolute;
    right: 54px;
    top: 1090px;
    font-family: "Open Sans", Arial, sans-serif;
    font-weight: 700;
    font-size: 37px;
    color: var(--sage-deep);
  }
</style>
</head>
<body>
  <main class="post">
    <svg class="wave" viewBox="0 0 1500 1500" aria-hidden="true">
      <path class="wave__band" d="M1500,55 C1380,115 1300,205 1270,400 C1240,600 1252,850 1140,962 C1050,1050 900,1062 780,1122 C620,1205 580,1320 545,1500 L1500,1500 Z"/>
      <path class="wave__fill" d="M1500,175 C1400,222 1350,350 1320,550 C1292,750 1290,850 1240,922 C1150,1080 1000,1102 880,1162 C760,1222 700,1330 665,1500 L1500,1500 Z"/>
    </svg>

    <h1 class="quote">
      <span class="quote__line"><span class="c-coral">Don’t</span> <span class="c-forest">go</span></span>
      <span class="quote__line c-clay">through</span>
      <span class="quote__line"><span class="c-blush">life,</span> <span class="c-sage">grow</span></span>
      <span class="quote__line c-mustard">through</span>
      <span class="quote__line c-brick">life.</span>
    </h1>

    <p class="author">Milo Pendrake</p>
    <p class="handle">@QuillmoreStudio</p>
  </main>
</body>
</html>
```